Bright Path Therapies business cards and stationary

Need business cards and stationary designed to match previously made logo for for a new company based in Sydney NSW called 'Bright Path Therapies'.

We provide early intervention services and diagnostic assessment for children with disability and their families. I would like designs that are colourful and child friendly - possibly using feet/footprints/steps on a white background. The final design should communicate that we are family friendly, accepting and fun to work with.

Target Market(s)

Parents and Families
Teachers
Allied Health Professionals

Industry/Entity Type

Psychology

Contact Information for Business Card

Bright Path Therapies
www.brightpaththerapies.example
info@brightpaththerapies.example

Font styles to use
Sans Serif
Decorative
Script

Requirements
Must have
• Match the font and colour scheme of logo, along with footprint picture
Nice to have
• Clean and simple, while reflecting that I am working with families.
• Also- editable for when we make staff specific cards.

```html
<!DOCTYPE html>
<html lang="en">
<head>
<meta charset="utf-8">
<title>Bright Path Therapies — Business Card</title>
<link href="https://fonts.googleapis.com/css2?family=Comic+Neue:wght@700&family=Mulish:wght@400;500&display=swap" rel="stylesheet">
<style>
  :root {
    --page-bg: #ece8e3;
    --card-bg: #f7f8fa;
    --brand-red: #d8232a;
    --brand-red-soft: #e9504c;
    --ink-navy: #1f3a7a;
    --ink-red: #d2262b;
  }
  * { margin: 0; padding: 0; box-sizing: border-box; }
  html, body {
    width: 1200px; height: 970px; overflow: hidden;
    background: var(--page-bg);
  }
  .card {
    position: absolute; left: 50px; top: 171px;
    width: 1100px; height: 628px;
    background: var(--card-bg);
    overflow: hidden;
    box-shadow: 0 6px 24px rgba(0,0,0,0.12);
    font-family: "Mulish", sans-serif;
  }
  .card__feature {
    position: absolute; left: 0; top: 0;
    width: 1100px; height: 628px;
  }
  .brand {
    position: absolute; left: 524px; top: 82px;
    display: flex; align-items: center; gap: 24px;
  }
  .brand__dot {
    width: 128px; height: 128px; border-radius: 50%;
    background: var(--brand-red);
    flex: none;
  }
  .brand__name {
    font-family: "Mulish", sans-serif; font-weight: 500;
    font-size: 44px; line-height: 1.12; color: var(--ink-navy);
    width: 340px;
  }
  .person {
    position: absolute; left: 524px; top: 336px;
  }
  .person__name {
    font-family: "Comic Neue", sans-serif; font-weight: 700;
    font-size: 40px; letter-spacing: 2px; color: var(--ink-red);
    line-height: 1;
  }
  .person__role {
    font-size: 29px; color: var(--ink-navy); line-height: 1.05;
  }
  .contacts {
    position: absolute; left: 524px; top: 464px;
    list-style: none;
  }
  .contacts__item {
    display: flex; align-items: center; gap: 18px;
    height: 38px;
    font-size: 29px; color: var(--ink-navy);
  }
  .contacts__icon {
    width: 30px; height: 30px; flex: none;
  }
</style>
</head>
<body>
  <div class="card">
    <svg class="card__feature" viewBox="0 0 1100 628" role="img" aria-label="Large red curved panel with footprint artwork">
      <defs>
        <linearGradient id="featureFill" x1="0" y1="0" x2="1" y2="1">
          <stop offset="0" stop-color="#d8232a"/>
          <stop offset="1" stop-color="#e9504c"/>
        </linearGradient>
      </defs>
      <path d="M0 0 H215 C330 40 500 190 480 330 C462 455 250 560 85 628 H0 Z" fill="url(#featureFill)"/>
    </svg>

    <div class="brand">
      <div class="brand__dot"></div>
      <div class="brand__name">Bright Path Therapies</div>
    </div>

    <div class="person">
      <div class="person__name">JORDAN BLAKE</div>
      <div class="person__role">Manager</div>
    </div>

    <ul class="contacts">
      <li class="contacts__item">
        <svg class="contacts__icon" viewBox="0 0 26 26" aria-hidden="true">
          <circle cx="13" cy="13" r="12" fill="none" stroke="#d8232a" stroke-width="2"/>
          <path d="M7 10 q6 -5 12 0 l-2 2 h-8 z M8 13 h10 v5 h-10 z" fill="#d8232a"/>
        </svg>
        <span>(555) 014 2290</span>
      </li>
      <li class="contacts__item">
        <svg class="contacts__icon" viewBox="0 0 26 26" aria-hidden="true">
          <circle cx="13" cy="13" r="12" fill="none" stroke="#d8232a" stroke-width="2"/>
          <rect x="7" y="9" width="12" height="8" fill="#d8232a"/>
          <path d="M7 9 l6 5 l6 -5" fill="none" stroke="#f7f8fa" stroke-width="1.2"/>
        </svg>
        <span>info@brightpaththerapies.example</span>
      </li>
      <li class="contacts__item">
        <svg class="contacts__icon" viewBox="0 0 26 26" aria-hidden="true">
          <circle cx="13" cy="13" r="12" fill="none" stroke="#d8232a" stroke-width="2"/>
          <circle cx="13" cy="13" r="7" fill="none" stroke="#d8232a" stroke-width="1.5"/>
          <path d="M6 13 h14 M13 6 v14 M13 6 q-4 7 0 14 M13 6 q4 7 0 14" fill="none" stroke="#d8232a" stroke-width="1.2"/>
        </svg>
        <span>www.brightpaththerapies.example</span>
      </li>
    </ul>
  </div>
</body>
</html>
```